Design for sports training app

We need the design for 9 screens of an app that supports trainers of sport teams in preparing their training sessions. Regarding colors, fonts etc. there is absolute freedom for the designer to choose what he thinks is best.
The app will be called "Plomix", our idea for the logo is something like a stopwatch.
Wireframes are attached for every screen. You don't have to stick to those - if you have better ideas, we are happy to see them.
Our strategy is "mobile first". Based on the app design we will create a homepage later - I guess it makes sense to give this to the same person, let's see.
The deliverables are attached.
All in all the main target is to present a very simple, intuitive and nice UI that the user can work with without much learning.
Updates
Target Market(s)
Soccer trainers
Industry/Entity Type
Training
Look and feel

```html
<!DOCTYPE html>
<html lang="en">
<head>
<meta charset="utf-8">
<title>KICKSTART – Training App Screens</title>
<link rel="stylesheet" href="https://fonts.googleapis.com/css2?family=Montserrat:wght@400;600;700&family=Quicksand:wght@400;500;600;700&display=swap">
<style>
:root{
  --stage:#d66d61;
  --stage-deep:#c45a50;
  --coral:#f47f6f;
  --dark:#222427;
  --dark-2:#2b2d31;
  --panel-top:#ececec;
  --panel-bottom:#d2d2d2;
  --band:#c9c9c9;
  --blue:#5cc6ee;
  --green:#46d9b0;
  --red:#f26b5e;
  --field:#8fdfa6;
  --ink:#333538;
  --muted:#9a9a9a;
  --line:#cfcfcf;
  --white:#ffffff;
}
*{box-sizing:border-box;margin:0;padding:0}
html,body{width:1200px;height:1200px;overflow:hidden}
body{position:relative;font-family:"Quicksand",sans-serif;color:var(--ink);background:var(--stage)}
.stage-backdrop{position:absolute;inset:0;background:radial-gradient(ellipse at 55% 35%,#e08478 0%,var(--stage) 45%,var(--stage-deep) 100%)}
.phone{position:absolute;width:220px;overflow:hidden;background:linear-gradient(var(--panel-top),var(--panel-bottom));box-shadow:0 4px 14px rgba(0,0,0,.18)}
.row-top{top:196px;height:394px}
.row-bottom{top:614px;height:391px}
.status{position:absolute;left:0;top:0;width:100%;height:11px;background:var(--dark);color:#c8c8c8;font-size:5.5px;font-family:"Montserrat",sans-serif;display:flex;align-items:center;justify-content:space-between;padding:0 5px;z-index:3}
.status .time{position:absolute;left:50%;transform:translateX(-50%)}
.status .batt{display:inline-block;width:9px;height:4px;border:1px solid #c8c8c8;margin-left:3px;vertical-align:middle}
.header{position:absolute;left:0;top:11px;width:100%;height:30px;background:var(--dark);color:var(--white);font-family:"Montserrat",sans-serif;font-weight:600;font-size:7.5px;display:flex;align-items:center;justify-content:center}
.header .back{position:absolute;left:10px;top:10px}
.header .edit{position:absolute;right:12px;font-size:7px}
.abs{position:absolute}
.label{font-size:6.5px;color:var(--ink);font-weight:600}
.small{font-size:5.6px;line-height:1.45;color:var(--ink);text-align:justify}
.muted{color:var(--muted)}
.pill{position:absolute;height:10px;border-radius:5px;color:var(--white);font-size:6px;font-weight:700;display:flex;align-items:center;justify-content:center}
.pill.blue{background:var(--blue)}
.pill.green{background:var(--green)}
.pill.red{background:var(--red)}
.list-row{position:absolute;left:0;width:100%;height:14px;display:flex;align-items:center;font-size:6.5px}
.list-row .bar{width:3px;height:100%;margin-right:10px}
.nav-row{position:absolute;left:10px;right:10px;display:flex;justify-content:space-between;font-size:6.5px;font-weight:700;border-bottom:1px solid var(--line);padding-bottom:4px}
.cta{position:absolute;left:0;width:100%;background:var(--coral);color:var(--white);font-family:"Montserrat",sans-serif;font-weight:600;font-size:8px;display:flex;align-items:center;justify-content:center;letter-spacing:.3px}
.tabbar{position:absolute;left:0;bottom:0;width:100%;height:34px;background:var(--dark-2);display:flex;justify-content:space-around;align-items:center}
.tab{display:flex;flex-direction:column;align-items:center;font-size:5px;color:#555;gap:2px}
.tab.active{color:var(--white)}
.diagram{position:absolute;background:var(--field)}
.media{position:absolute;background:linear-gradient(135deg,#2f6b3c,#4f8f55 60%,#6ea46a)}
/* skills */
.skill{position:absolute;left:0;width:100%;height:34px}
.skill .name{position:absolute;left:12px;top:0;font-size:6px;color:var(--muted)}
.skill .pct{position:absolute;top:0;font-size:7px;color:var(--coral);font-weight:600}
.skill .min{position:absolute;left:13px;top:13px;font-size:5.5px;color:var(--muted)}
.skill .max{position:absolute;left:202px;top:13px;font-size:5.5px;color:var(--muted)}
.skill .track{position:absolute;left:25px;top:14px;width:170px;height:5px;border-radius:3px;background:#f2f2f2;box-shadow:inset 0 1px 2px rgba(0,0,0,.15)}
.skill .fill{position:absolute;left:0;top:0;height:100%;border-radius:3px;background:var(--coral)}
.skill .thumb{position:absolute;top:-3px;width:11px;height:11px;border-radius:50%;background:#f4f4f4;box-shadow:0 1px 2px rgba(0,0,0,.35);margin-left:-5px}
.req-row{position:absolute;left:14px;right:14px;height:22px;border-bottom:1px solid var(--line);display:flex;align-items:center;justify-content:space-between;font-size:7px;font-weight:600}
.req-row .count{color:var(--muted);font-weight:400;font-size:6.5px}
.stepper{display:flex;align-items:center;gap:10px}
.step{width:9px;height:9px;border-radius:50%;background:#e2e2e2;color:#bbb;font-size:5px;display:flex;align-items:center;justify-content:center}
.step.on{background:var(--red);color:var(--white)}
.brand-name{font-family:"Montserrat",sans-serif;font-weight:700;color:var(--white)}
.brand-dot{border-radius:50%;border:2px solid var(--white)}
.field-line{position:absolute;left:24px;right:24px;border-bottom:1px solid #555;font-size:6px;color:#ddd;padding-bottom:5px;display:flex;justify-content:space-between}
.club-badge{position:absolute;border-radius:50%;background:var(--white);border:2px solid var(--coral)}
.strength{position:absolute;left:14px;font-size:6px;line-height:10.5px}
.strength b{display:inline-block;width:70px;text-align:right;margin-right:6px}
</style>
</head>
<body>
<div class="stage-backdrop" role="img" aria-label="Coral-tinted photo of a soccer player kicking a ball"></div>

<!-- Screen: splash -->
<section class="phone row-top" style="left:36px;background:#161718">
  <div class="status"><span>●●○○○ NetCell</span><span class="time">14:39</span><span>◎<i class="batt"></i></span></div>
  <div class="abs" style="left:0;top:11px;width:220px;height:383px;background:radial-gradient(ellipse at 45% 35%,#3a3b3d,#161718 70%)" role="img" aria-label="Dark photo of a soccer player in motion"></div>
  <div class="abs" style="left:40px;top:185px;display:flex;align-items:center;gap:8px">
    <span class="brand-dot" style="width:24px;height:24px"></span>
    <span class="brand-name" style="font-size:24px;letter-spacing:.5px">KICKSTART</span>
  </div>
</section>

<!-- Screen: login -->
<section class="phone row-top" style="left:264px;background:radial-gradient(ellipse at 40% 60%,#2c2d2f,#141516 75%)">
  <div class="status"><span>●●○○○ NetCell</span><span class="time">14:39</span><span>◎<i class="batt"></i></span></div>
  <div class="abs" style="left:0;top:130px;width:220px;height:264px;background:radial-gradient(ellipse at 30% 70%,#2a2b2d,transparent 70%)" role="img" aria-label="Dark photo of a soccer player"></div>
  <span class="abs brand-dot" style="left:94px;top:44px;width:32px;height:32px"></span>
  <div class="abs brand-name" style="left:0;top:90px;width:220px;text-align:center;font-size:12px">KICKSTART</div>
  <p class="abs" style="left:16px;top:115px;width:188px;text-align:center;font-size:5.4px;color:#fff;font-weight:700;line-height:1.35">The Kickstart success formula is an intense and motivating atmosphere that is designed for athletes, young and old.</p>
  <div class="field-line" style="top:160px"><span>Email / Username</span><svg width="9" height="7" viewBox="0 0 9 7"><polyline points="1,4 3.5,6 8,1" fill="none" stroke="#46d9b0" stroke-width="1"/></svg></div>
  <div class="field-line" style="top:191px"><span>Password</span><span style="color:var(--coral)">Forgot?</span></div>
  <div class="cta" style="left:36px;width:148px;top:236px;height:28px;border-radius:2px;font-size:10px">Login</div>
  <div class="abs" style="left:0;top:296px;width:220px;text-align:center;font-size:6px;color:#fff">Don't have a account? <b style="color:var(--coral)">SignUp</b></div>
</section>

<!-- Screen: dashboard -->
<section class="phone row-top" style="left:489px">
  <div class="status"><span>●●○○○ NetCell</span><span class="time">14:39</span><span>◎<i class="batt"></i></span></div>
  <div class="abs" style="left:0;top:11px;width:220px;height:118px;background:var(--dark)"></div>
  <span class="club-badge" style="left:13px;top:24px;width:34px;height:34px"></span>
  <div class="abs" style="left:55px;top:29px;font-size:7.5px;color:#fff">FC Lindenau – Juniors</div>
  <div class="abs" style="left:55px;top:42px;font-size:6.5px;color:#ddd;display:flex;align-items:center;gap:3px"><svg width="6" height="7" viewBox="0 0 6 7"><path d="M3 .5a2.3 2.3 0 0 1 2.3 2.3C5.3 4.5 3 6.5 3 6.5S.7 4.5.7 2.8A2.3 2.3 0 0 1 3 .5z" fill="none" stroke="#ddd" stroke-width=".8"/></svg>Riverton, USA</div>
  <svg class="abs" style="left:198px;top:24px" width="11" height="11" viewBox="0 0 11 11"><circle cx="5.5" cy="5.5" r="3.6" fill="none" stroke="#ccc" stroke-width="1" stroke-dasharray="2 1"/><circle cx="5.5" cy="5.5" r="1.3" fill="none" stroke="#ccc" stroke-width=".8"/></svg>
  <div class="abs" style="left:162px;top:56px;font-size:16px;color:#fff">30°</div>
  <div class="abs" style="left:15px;top:74px;width:32px;height:32px;background:#f4f4f4;border-radius:2px;overflow:hidden;text-align:center">
    <div style="background:var(--coral);color:#fff;font-size:5px;height:9px;line-height:9px">APR</div>
    <div style="font-size:10px;font-weight:700;line-height:20px">26</div>
  </div>
  <div class="abs" style="left:18px;top:111px;font-size:7.5px;color:#fff">17:30</div>
  <div class="abs" style="left:65px;top:78px;width:1px;height:38px;background:#444"></div>
  <svg class="abs" style="left:85px;top:74px" width="28" height="22" viewBox="0 0 28 22"><circle cx="17" cy="8" r="4" fill="none" stroke="#fff" stroke-width="1"/><path d="M6 19h14a4 4 0 0 0 0-8 6 6 0 0 0-11.5 1A3.5 3.5 0 0 0 6 19z" fill="var(--dark)" stroke="#fff" stroke-width="1"/></svg>
  <div class="abs" style="left:83px;top:100px;font-size:6.5px;color:#fff">Cloudy</div>
  <div class="abs" style="left:128px;top:80px;font-size:6.5px;color:#ddd;line-height:10.8px;text-align:right;width:40px">Feel like<br>Humidity<br>Pressure<br>Precipitation</div>
  <div class="abs" style="left:172px;top:80px;font-size:6.5px;color:#ddd;line-height:10.8px">38°<br>63%<br>30.10 in<br>0% in</div>
  <div class="abs" style="left:69px;top:146px;width:84px;height:84px;border-radius:50%;background:radial-gradient(circle at 40% 35%,#fff,#e3e3e3);box-shadow:0 6px 10px rgba(0,0,0,.2)" role="img" aria-label="Start training button"></div>
  <svg class="abs" style="left:166px;top:142px" width="15" height="15" viewBox="0 0 15 15"><path d="M12 7.5A4.5 4.5 0 1 1 9.5 3.5" fill="none" stroke="#777" stroke-width="1.3"/><polyline points="8,1.5 10.5,3.6 8.3,5.8" fill="none" stroke="#777" stroke-width="1.3"/></svg>
  <div class="abs label" style="left:10px;top:242px">Elements</div>
  <div class="list-row" style="top:257px"><span class="bar" style="background:var(--blue)"></span>WARM-UP</div>
  <div class="list-row" style="top:277px"><span class="bar" style="background:var(--blue)"></span>4 Vs. 2</div>
  <div class="list-row" style="top:296px"><span class="bar" style="background:var(--blue)"></span>Offensive 2 vs. 1</div>
  <div class="list-row" style="top:316px"><span class="bar" style="background:var(--blue)"></span>Game 7 on 7</div>
  <div class="pill blue" style="left:102px;top:259px;width:46px">20 min</div>
  <div class="pill blue" style="left:102px;top:279px;width:46px">25 min</div>
  <div class="pill blue" style="left:102px;top:298px;width:46px">20 min</div>
  <div class="pill blue" style="left:102px;top:318px;width:46px">25 min</div>
  <svg class="abs" style="left:195px;top:259px" width="11" height="70" viewBox="0 0 11 70"><g fill="none" stroke="#999" stroke-width="1"><path d="M9 5.5A3.5 3.5 0 1 1 7 2.3"/><path d="M9 25.5A3.5 3.5 0 1 1 7 22.3"/><path d="M9 44.5A3.5 3.5 0 1 1 7 41.3"/><path d="M9 64.5A3.5 3.5 0 1 1 7 61.3"/></g></svg>
  <div class="nav-row" style="top:344px"><span>Plomix Skills</span><span>›</span></div>
  <div class="nav-row" style="top:366px;border:0"><span>Prerequisites</span><span>›</span></div>
</section>

<!-- Screen: session -->
<section class="phone row-top" style="left:717px">
  <div class="status"><span>●●○○○ NetCell</span><span class="time">14:39</span><span>◎<i class="batt"></i></span></div>
  <div class="header"><svg class="back" width="6" height="10" viewBox="0 0 6 10"><polyline points="5,1 1,5 5,9" fill="none" stroke="#fff" stroke-width="1.2"/></svg>14 Apr 2016, 15:24 hr</div>
  <div class="abs label" style="left:10px;top:54px">Elements</div>
  <div class="list-row" style="top:70px"><span class="bar" style="background:var(--green)"></span>WARM-UP</div>
  <div class="list-row" style="top:90px"><span class="bar" style="background:var(--red)"></span>4 Vs. 2</div>
  <div class="list-row" style="top:109px"><span class="bar" style="background:var(--green)"></span>Offensive 2 vs. 1</div>
  <div class="list-row" style="top:129px"><span class="bar" style="background:var(--blue)"></span>Game 7 on 7</div>
  <div class="pill green" style="left:101px;top:72px;width:46px"><svg width="10" height="7" viewBox="0 0 10 7"><polyline points="1,4 4,6 9,1" fill="none" stroke="#fff" stroke-width="1"/></svg></div>
  <div class="pill red" style="left:101px;top:92px;width:46px">4.5 min</div>
  <div class="pill green" style="left:101px;top:111px;width:46px">11 min</div>
  <div class="pill blue" style="left:101px;top:131px;width:46px">25 min</div>
  <div class="abs" style="left:198px;top:71px;font-size:8px;line-height:19.5px;color:#555">›<br>›<br>›<br>›</div>
  <div class="abs" style="left:0;top:159px;width:220px;height:17px;background:var(--band);font-family:'Montserrat',sans-serif;font-weight:600;font-size:7.5px;display:flex;align-items:center;justify-content:center">Offensive 2 vs. 1</div>
  <div class="diagram" style="left:13px;top:182px;width:194px;height:122px" role="img" aria-label="Play diagram Spin 3MO 45 FB Dive with player positions and routes"></div>
  <div class="abs" style="left:13px;top:184px;width:194px;text-align:center;font-size:7px;font-weight:700;color:#1e3b22">Spin 3MO 45 FB Dive</div>
  <p class="abs small" style="left:14px;top:312px;width:192px;height:46px;overflow:hidden">Lorem Ipsum is simply dummy text of the printing and typesetting industry. Lorem Ipsum has been the industry's standard dummy text ever since the 1500s, when an unknown printer took a galley of type and scrambled it to make a type specimen book. It has survived not only five centuries, but also</p>
  <div class="cta" style="top:360px;height:34px">FINISH TRAINING</div>
</section>

<!-- Screen: drill info -->
<section class="phone row-top" style="left:945px">
  <div class="status"><span>●●○○○ NetCell</span><span class="time">14:39</span><span>◎<i class="batt"></i></span></div>
  <div class="header"><svg class="back" width="6" height="10" viewBox="0 0 6 10"><polyline points="5,1 1,5 5,9" fill="none" stroke="#fff" stroke-width="1.2"/></svg>Offensive 2 vs. 1</div>
  <div class="diagram" style="left:14px;top:41px;width:192px;height:79px" role="img" aria-label="Play diagram with player positions and routes"></div>
  <div class="abs muted" style="left:14px;top:129px;font-size:6px">Strength</div>
  <div class="strength" style="top:140px;left:-10px"><b>Speed Warm-up :</b>45-60 min<br><b>Snatch :</b>3 x (3-4) x 30% – 50%<br><b>sqaut :</b>4-5 x (1-10) x 60% – 100%<br><b>RDL :</b>3 x 5 x 50% – 65%</div>
  <p class="abs small" style="left:10px;top:186px;width:200px">My Oakdale Hawks team ran this play to perfection with two big fullbacks rotating in to keep them fresh for blocking and running this play all over our opponent's defenses. Depending of the defensive alignments of the defenses d-tackles you either run to the 5 or 3 holes for a nice gainer from your fullbacks. You can also run the play from Double Tights or a traditional Spread. I personally like to run it from the Nasty Spread as shown below. The play is set up by the Spin Sweeps, Counters and Reverses. You want to lull the defense to sleep then hit them with a quick FB dive.</p>
  <div class="abs muted" style="left:14px;top:290px;font-size:6px">Video</div>
  <div class="media" style="left:14px;top:304px;width:192px;height:54px" role="img" aria-label="Video still of a soccer match"></div>
  <div class="tabbar">
    <div class="tab active"><svg width="18" height="14" viewBox="0 0 18 14"><rect x="1" y="3" width="13" height="10" fill="none" stroke="#fff" stroke-width="1"/><polyline points="4,1 16,1 16,10" fill="none" stroke="#fff" stroke-width="1"/><polygon points="6,6 6,11 10,8.5" fill="#fff"/></svg>Info</div>
    <div class="tab"><svg width="18" height="12" viewBox="0 0 18 12"><g stroke="#555" stroke-width="1.5"><line x1="1" y1="2" x2="17" y2="2"/><line x1="1" y1="6" x2="13" y2="6"/><line x1="1" y1="10" x2="17" y2="10"/></g></svg>Skills</div>
    <div class="tab"><svg width="14" height="14" viewBox="0 0 14 14"><circle cx="6" cy="6" r="4.5" fill="none" stroke="#555" stroke-width="1.5"/><line x1="9.3" y1="9.3" x2="13" y2="13" stroke="#555" stroke-width="1.5"/></svg>Prerequisites</div>
  </div>
</section>

<!-- Screen: skills overview -->
<section class="phone row-bottom" style="left:36px">
  <div class="status"><span>●●○○○ NetCell</span><span class="time">14:39</span><span>◎<i class="batt"></i></span></div>
  <div class="header"><svg class="back" width="6" height="10" viewBox="0 0 6 10"><polyline points="5,1 1,5 5,9" fill="none" stroke="#fff" stroke-width="1.2"/></svg>Offensive 2 vs. 1</div>
  <p class="abs small" style="left:14px;top:55px;width:192px">Lorem Ipsum is simply dummy text of the printing and typesetting industry. Lorem Ipsum has been the industry's standard dummy text ever since the</p>
  <div class="skill" style="top:103px"><span class="name">Coordination</span><span class="pct" style="left:99px">25 %</span><span class="min">0</span><div class="track"><div class="fill" style="width:25%"></div></div><span class="max">100</span></div>
  <div class="skill" style="top:142px"><span class="name">Finishing</span><span class="pct" style="left:99px">83 %</span><span class="min">0</span><div class="track"><div class="fill" style="width:83%"></div></div><span class="max">100</span></div>
  <div class="skill" style="top:180px"><span class="name">Stamina</span><span class="pct" style="left:99px">75 %</span><span class="min">0</span><div class="track"><div class="fill" style="width:75%"></div></div><span class="max">100</span></div>
  <div class="skill" style="top:219px"><span class="name">Speed</span><span class="pct" style="left:99px">90 %</span><span class="min">0</span><div class="track"><div class="fill" style="width:90%"></div></div><span class="max">100</span></div>
  <div class="skill" style="top:257px"><span class="name">Understanding of Game</span><span class="pct" style="left:131px">75 %</span><span class="min">0</span><div class="track"><div class="fill" style="width:75%"></div></div><span class="max">100</span></div>
  <div class="skill" style="top:296px"><span class="name">Devensive Behavior</span><span class="pct" style="left:99px">90 %</span><span class="min">0</span><div class="track"><div class="fill" style="width:90%"></div></div><span class="max">100</span></div>
  <div class="tabbar">
    <div class="tab"><svg width="18" height="14" viewBox="0 0 18 14"><rect x="1" y="3" width="13" height="10" fill="none" stroke="#555" stroke-width="1"/><polyline points="4,1 16,1 16,10" fill="none" stroke="#555" stroke-width="1"/><polygon points="6,6 6,11 10,8.5" fill="#555"/></svg>Info</div>
    <div class="tab active"><svg width="18" height="12" viewBox="0 0 18 12"><g stroke="#fff" stroke-width="1.5"><line x1="1" y1="2" x2="17" y2="2"/><line x1="1" y1="6" x2="13" y2="6"/><line x1="1" y1="10" x2="17" y2="10"/></g></svg>Skills</div>
    <div class="tab"><svg width="14" height="14" viewBox="0 0 14 14"><circle cx="6" cy="6" r="4.5" fill="none" stroke="#555" stroke-width="1.5"/><line x1="9.3" y1="9.3" x2="13" y2="13" stroke="#555" stroke-width="1.5"/></svg>Prerequisites</div>
  </div>
</section>

<!-- Screen: prerequisites -->
<section class="phone row-bottom" style="left:264px">
  <div class="status"><span>●●○○○ NetCell</span><span class="time">14:39</span><span>◎<i class="batt"></i></span></div>
  <div class="header"><svg class="back" width="6" height="10" viewBox="0 0 6 10"><polyline points="5,1 1,5 5,9" fill="none" stroke="#fff" stroke-width="1.2"/></svg>Offensive 2 vs. 1</div>
  <div class="req-row" style="top:61px;left:14px;right:24px"><span>Cones</span><span class="count">20</span></div>
  <div class="req-row" style="top:88px;left:14px;right:24px"><span>Goals</span><span class="count">4</span></div>
  <div class="req-row" style="top:115px;left:14px;right:24px"><span>Players</span><span class="count">18</span></div>
  <div class="req-row" style="top:142px;left:14px;right:24px;border:0"><span>Goalies</span><span class="count">6</span></div>
  <div class="tabbar">
    <div class="tab"><svg width="18" height="14" viewBox="0 0 18 14"><rect x="1" y="3" width="13" height="10" fill="none" stroke="#555" stroke-width="1"/><polyline points="4,1 16,1 16,10" fill="none" stroke="#555" stroke-width="1"/><polygon points="6,6 6,11 10,8.5" fill="#555"/></svg>Info</div>
    <div class="tab"><svg width="18" height="12" viewBox="0 0 18 12"><g stroke="#555" stroke-width="1.5"><line x1="1" y1="2" x2="17" y2="2"/><line x1="1" y1="6" x2="13" y2="6"/><line x1="1" y1="10" x2="17" y2="10"/></g></svg>Skills</div>
    <div class="tab active"><svg width="14" height="14" viewBox="0 0 14 14"><circle cx="6" cy="6" r="4.5" fill="none" stroke="#fff" stroke-width="1.5"/><line x1="9.3" y1="9.3" x2="13" y2="13" stroke="#fff" stroke-width="1.5"/></svg>Prerequisites</div>
  </div>
</section>

<!-- Screen: skill editor -->
<section class="phone row-bottom" style="left:489px">
  <div class="status"><span>●●○○○ NetCell</span><span class="time">14:39</span><span>◎<i class="batt"></i></span></div>
  <div class="header"><svg class="back" width="6" height="10" viewBox="0 0 6 10"><polyline points="5,1 1,5 5,9" fill="none" stroke="#fff" stroke-width="1.2"/></svg>Plomix Skills</div>
  <p class="abs small" style="left:14px;top:55px;width:192px">Lorem Ipsum is simply dummy text of the printing and typesetting industry. Lorem Ipsum has been the industry's standard dummy text ever since the</p>
  <div class="skill" style="top:103px"><span class="name">Coordination</span><span class="pct" style="left:99px">25 %</span><span class="min">0</span><div class="track"><div class="fill" style="width:33%"></div><span class="thumb" style="left:33%"></span></div><span class="max">100</span></div>
  <div class="skill" style="top:142px"><span class="name">Finishing</span><span class="pct" style="left:99px">83 %</span><span class="min">0</span><div class="track"><div class="fill" style="width:72%"></div><span class="thumb" style="left:72%"></span></div><span class="max">100</span></div>
  <div class="skill" style="top:180px"><span class="name">Stamina</span><span class="pct" style="left:99px">75 %</span><span class="min">0</span><div class="track"><div class="fill" style="width:63%"></div><span class="thumb" style="left:63%"></span></div><span class="max">100</span></div>
  <div class="skill" style="top:219px"><span class="name">Speed</span><span class="pct" style="left:99px">90 %</span><span class="min">0</span><div class="track"><div class="fill" style="width:86%"></div><span class="thumb" style="left:86%"></span></div><span class="max">100</span></div>
  <div class="skill" style="top:257px"><span class="name">Understanding of Game</span><span class="pct" style="left:131px">75 %</span><span class="min">0</span><div class="track"><div class="fill" style="width:64%"></div><span class="thumb" style="left:64%"></span></div><span class="max">100</span></div>
  <div class="skill" style="top:296px"><span class="name">Devensive Behavior</span><span class="pct" style="left:99px">90 %</span><span class="min">0</span><div class="track"><div class="fill" style="width:86%"></div><span class="thumb" style="left:86%"></span></div><span class="max">100</span></div>
</section>

<!-- Screen: prerequisites editor -->
<section class="phone row-bottom" style="left:717px">
  <div class="status"><span>●●○○○ NetCell</span><span class="time">14:39</span><span>◎<i class="batt"></i></span></div>
  <div class="header"><svg class="back" width="6" height="10" viewBox="0 0 6 10"><polyline points="5,1 1,5 5,9" fill="none" stroke="#fff" stroke-width="1.2"/></svg>Offensive 2 vs. 1</div>
  <div class="req-row" style="top:61px"><span>Cones</span><span class="stepper"><span class="step">«</span><span class="count">20</span><span class="step on">»</span></span></div>
  <div class="req-row" style="top:88px"><span>Goals</span><span class="stepper"><span class="step">«</span><span class="count">&nbsp;4&nbsp;</span><span class="step">»</span></span></div>
  <div class="req-row" style="top:115px"><span>Players</span><span class="stepper"><span class="step">«</span><span class="count">18</span><span class="step">»</span></span></div>
  <div class="req-row" style="top:142px"><span>Goalies</span><span class="stepper"><span class="step">«</span><span class="count">&nbsp;6&nbsp;</span><span class="step">»</span></span></div>
</section>

<!-- Screen: settings -->
<section class="phone row-bottom" style="left:945px">
  <div class="status"><span>●●○○○ NetCell</span><span class="time">14:39</span><span>◎<i class="batt"></i></span></div>
  <div class="header"><svg class="back" width="6" height="10" viewBox="0 0 6 10"><polyline points="5,1 1,5 5,9" fill="none" stroke="#fff" stroke-width="1.2"/></svg>Settings<span class="edit">Edit</span></div>
  <span class="club-badge" style="left:84px;top:52px;width:53px;height:53px"></span>
  <div class="abs" style="left:0;top:114px;width:220px;text-align:center;font-size:7.5px;font-weight:600">FC Lindenau – Juniors</div>
  <div class="abs" style="left:0;top:129px;width:220px;text-align:center;font-size:6.5px;font-weight:600;display:flex;justify-content:center;align-items:center;gap:4px"><svg width="6" height="7" viewBox="0 0 6 7"><path d="M3 .5a2.3 2.3 0 0 1 2.3 2.3C5.3 4.5 3 6.5 3 6.5S.7 4.5.7 2.8A2.3 2.3 0 0 1 3 .5z" fill="none" stroke="#333" stroke-width=".8"/></svg>Riverton, USA</div>
  <div class="abs" style="left:14px;top:150px;font-size:6.5px"><b>Loged in as</b>&nbsp;&nbsp;&nbsp;&nbsp;&nbsp;Karl Brenner</div>
  <div class="abs" style="left:14px;top:173px;font-size:6.5px;font-weight:700">About Team</div>
  <p class="abs small" style="left:8px;top:186px;width:204px;font-size:6.2px;line-height:1.32">Lorem Ipsum is simply dummy text of the printing and typesetting industry. Lorem Ipsum has been the industry's standard dummy text ever since the 1500s, when an unknown printer took a galley of type and scrambled it to make a type specimen book. It has survived not only five centuries, but also the leap into electronic typesetting, remaining essentially unchanged. It was popularised in the 1960s with the release of Printline</p>
  <div class="abs" style="left:0;top:291px;width:220px;height:17px;background:var(--band);display:flex;justify-content:space-between;align-items:center;padding:0 13px;font-size:6.5px;font-weight:700"><span>Legal</span><span>›</span></div>
  <div class="abs" style="left:0;top:310px;width:220px;height:17px;background:var(--band);display:flex;justify-content:space-between;align-items:center;padding:0 13px;font-size:6.5px;font-weight:700"><span>Share</span><span>›</span></div>
  <div class="cta" style="top:359px;height:32px">LOGOUT</div>
</section>
</body>
</html>
```